Hvac and insulation company needs good looking business card design

We are hvac and insulation company and looking for a new business cards that look to today standards designs

Target Market(s)

homeowners

Industry/Entity Type

Hvac

Contact Information for Business Card

Name: Dorian Velkova
Home comfort consultant
address: 4827 Marrow Ridge Rd #215 Alder Bay, CA 95412
office: 888-317-5069
cell: 510-642-1388
Lic.# 458127
Email: dorian@quarry-hvac.com
Web: quarry-hvac.com

Requirements
Must have
• clean and sleek look
Nice to have
• simple with a clean look
Should not have
• to busy business card

```html
<!DOCTYPE html>
<html lang="en">
<head>
<meta charset="utf-8">
<title>Quarry Home Solutions – Business Card</title>
<link href="https://fonts.googleapis.com/css2?family=Lato:wght@400;700&display=swap" rel="stylesheet">
<style>
  :root {
    --backdrop: #2c4766;
    --brand-orange: #f58720;
    --card-grey: #7d7d7d;
    --ink-white: #ffffff;
    --rule: #e6e6e6;
  }
  html, body {
    margin: 0;
    padding: 0;
    width: 1200px;
    height: 1000px;
    overflow: hidden;
    background: var(--backdrop);
    font-family: "Lato", sans-serif;
    color: var(--ink-white);
  }
  .canvas {
    position: relative;
    width: 1200px;
    height: 1000px;
  }
  .card {
    position: absolute;
    left: 280px;
    width: 640px;
    height: 365px;
    box-shadow: 0 14px 30px rgba(0, 0, 0, 0.35);
    box-sizing: border-box;
  }
  .card-front {
    top: 110px;
    background: var(--brand-orange);
  }
  .card-back {
    top: 525px;
    background: var(--card-grey);
  }
  .brand {
    position: absolute;
    display: flex;
    align-items: center;
    gap: 14px;
    font-weight: 700;
    color: var(--ink-white);
    white-space: nowrap;
  }
  .brand-mark {
    background: var(--ink-white);
    flex: none;
  }
  .card-front .brand {
    left: 0;
    right: 0;
    top: 150px;
    justify-content: center;
    font-size: 40px;
  }
  .card-front .brand-mark {
    width: 40px;
    height: 40px;
  }
  .front-web {
    position: absolute;
    left: 0;
    right: 0;
    bottom: 20px;
    text-align: center;
    font-size: 19px;
  }
  .card-back .brand {
    right: 28px;
    top: 74px;
    font-size: 26px;
    gap: 10px;
  }
  .card-back .brand-mark {
    width: 26px;
    height: 26px;
  }
  .person {
    position: absolute;
    left: 34px;
    top: 105px;
  }
  .person-name {
    font-size: 35px;
    line-height: 1.1;
    margin: 0;
    font-weight: 400;
  }
  .person-role {
    font-size: 19px;
    margin: 2px 0 0;
  }
  .divider {
    position: absolute;
    left: 32px;
    right: 28px;
    top: 180px;
    height: 2px;
    background: var(--rule);
  }
  .address {
    position: absolute;
    right: 26px;
    top: 188px;
    text-align: right;
    font-size: 17px;
    line-height: 24px;
    margin: 0;
    font-style: normal;
  }
  .contacts {
    position: absolute;
    left: 34px;
    top: 226px;
    margin: 0;
    padding: 0;
    list-style: none;
    font-size: 22px;
  }
  .contacts li {
    display: flex;
    align-items: center;
    gap: 14px;
    height: 33px;
  }
  .contacts svg {
    width: 20px;
    height: 20px;
    flex: none;
    fill: var(--ink-white);
  }
  .license {
    position: absolute;
    right: 26px;
    top: 310px;
    font-size: 17px;
  }
</style>
</head>
<body>
<main class="canvas">
  <section class="card card-front" aria-label="Card front">
    <div class="brand"><span class="brand-mark"></span>Quarry Home Solutions</div>
    <div class="front-web">www.quarry-hvac.com</div>
  </section>

  <section class="card card-back" aria-label="Card back">
    <div class="brand"><span class="brand-mark"></span>Quarry Home Solutions</div>
    <div class="person">
      <h1 class="person-name">Dorian Velkova</h1>
      <p class="person-role">Home comfort consultant</p>
    </div>
    <div class="divider"></div>
    <address class="address">4827 Marrow Ridge Rd #215 Alder Bay,<br>CA 95412</address>
    <ul class="contacts">
      <li>
        <svg viewBox="0 0 24 24" aria-hidden="true"><path d="M3 8c0-2 4-4 9-4s9 2 9 4v2h-5V8H8v2H3z M6 11h12l2 9H4z"/><circle cx="12" cy="15" r="2.5" fill="#7d7d7d"/></svg>
        888-317-5069
      </li>
      <li>
        <svg viewBox="0 0 24 24" aria-hidden="true"><path d="M6.6 10.8a15 15 0 0 0 6.6 6.6l2.2-2.2c.3-.3.7-.4 1-.2 1.1.4 2.300.6 3.6.6.6 0 1 .4 1 1V20c0 .6-.4 1-1 1A17 17 0 0 1 3 4c0-.6.4-1 1-1h3.5c.6 0 1 .4 1 1 0 1.3.2 2.5.6 3.6.1.3 0 .7-.2 1z"/></svg>
        510-642-1388
      </li>
      <li>
        <svg viewBox="0 0 24 24" aria-hidden="true"><path d="M3 6h18v12H3z"/><path d="M3 6l9 7 9-7" fill="none" stroke="#7d7d7d" stroke-width="1.6"/></svg>
        dorian@quarry-hvac.com
      </li>
    </ul>
    <div class="license">Lic.# 458127</div>
  </section>
</main>
</body>
</html>
```